My Coffee beans packaging design

Our company named Tamsel Coffee,We are a new coffee Roasters in CHINA. We need a packaging design for our new coffee beans we roasted.We would like to see designs that use bright color. The final design should communicate the professional and modern sense.We want to catch customers eyes.We would like it is outstanding.It is a freestyle design project.We would like to see different styles.Thank you for reading our requirement.
Updates

Reason: Thank you for designing these for us,we want some more design.

Target Market(s)

All the people who love coffee

Industry/Entity Type

Coffee Shop

Font styles to use
Serif
Sans Serif
Decorative
Script

Requirements
Must have
• We do not have anything must haves.
Nice to have
• We do not have anything must haves
Should not have
• We do not have anything mustn't haves

```html
<!DOCTYPE html>
<html lang="en">
<head>
<meta charset="UTF-8">
<title>Tamsel Coffee – Slow Roasted Espresso</title>
<link rel="stylesheet" href="https://fonts.googleapis.com/css2?family=Cinzel:wght@600&family=Playfair+Display:wght@400;700&family=Cormorant+Garamond:wght@600&display=swap">
<style>
  :root {
    --backdrop: #ffffff;
    --bag-black: #121212;
    --bag-edge: #1c1c1c;
    --teal: #2fb3aa;
    --teal-soft: #1f7f79;
    --white: #f4f4f4;
    --valve: #0b0b0b;
  }
  * { margin: 0; padding: 0; box-sizing: border-box; }
  html, body {
    width: 900px;
    height: 1200px;
    overflow: hidden;
    background: var(--backdrop);
  }
  .canvas {
    position: relative;
    width: 900px;
    height: 1200px;
    display: flex;
    align-items: center;
    justify-content: center;
  }
  .bag-front {
    position: relative;
    width: 620px;
    height: 1160px;
    background: var(--bag-black);
    border-top: 14px solid var(--bag-edge);
    display: flex;
    flex-direction: column;
    align-items: center;
  }
  .aroma-valve {
    position: absolute;
    top: 280px;
    left: 50%;
    transform: translateX(-50%);
  }
  .label-illustration {
    position: absolute;
    top: 400px;
    left: 50%;
    transform: translateX(-50%);
    width: 260px;
    height: 270px;
    border-radius: 50% 50% 46% 46%;
    background: radial-gradient(ellipse at 50% 45%, var(--teal-soft) 0%, rgba(31,127,121,0.35) 55%, rgba(18,18,18,0) 75%);
  }
  .brand-name {
    position: absolute;
    top: 705px;
    width: 100%;
    text-align: center;
    font-family: "Cinzel", serif;
    font-weight: 600;
    color: var(--teal);
    line-height: 1;
  }
  .brand-name .brand-main {
    display: block;
    font-size: 58px;
    letter-spacing: 6px;
  }
  .brand-name .brand-sub {
    display: block;
    margin-top: 10px;
    font-size: 22px;
    letter-spacing: 7px;
  }
  .roast-line {
    position: absolute;
    top: 820px;
    width: 100%;
    text-align: center;
    font-family: "Playfair Display", serif;
    font-weight: 700;
    font-size: 22px;
    letter-spacing: 2px;
    color: var(--white);
  }
  .product-name {
    position: absolute;
    top: 850px;
    width: 100%;
    text-align: center;
    font-family: "Cormorant Garamond", serif;
    font-weight: 600;
    font-size: 52px;
    letter-spacing: 2px;
    color: var(--teal);
  }
  .origin-line {
    position: absolute;
    top: 940px;
    width: 100%;
    text-align: center;
    font-family: "Playfair Display", serif;
    font-weight: 400;
    font-size: 17px;
    letter-spacing: 2px;
    color: var(--white);
  }
</style>
</head>
<body>
  <main class="canvas">
    <section class="bag-front">
      <svg class="aroma-valve" width="52" height="52" viewBox="0 0 52 52" aria-hidden="true">
        <circle cx="26" cy="26" r="24" fill="var(--valve)" stroke="#1e1e1e" stroke-width="2"/>
        <circle cx="26" cy="26" r="5" fill="#000"/>
      </svg>

      <div class="label-illustration" role="img" aria-label="Teal line illustration of a woman with flowing hair sipping from a coffee cup"></div>

      <h1 class="brand-name">
        <span class="brand-main">TAMSEL</span>
        <span class="brand-sub">COFFEE</span>
      </h1>

      <p class="roast-line">SLOW ROASTED</p>
      <p class="product-name">espresso</p>
      <p class="origin-line">MADE IN CHINA</p>
    </section>
  </main>
</body>
</html>
```